Nightclub-type Event Poster Advertisement

Lumora Events is based in Christchurch, New Zealand and we have our next party coming up. We like a different flair for each of our events so are looking for some help from you guys. We are very flexible with everything - colours, layout, backgrounds, fonts, etc so it's ALL up to you. Attached is our company logo and the flyer (and poster) we used for our last party. Our website is lumoranz.example where you can find and use our photos and find more info about us if you desire.
Designs we are wanting: An A3 poster,an A6 flyer (smaller version of the poster is probably fine), tickets (140x68 mm). It would be great if a 5 mm bleed was included so we could get them printed directly.
Details for the event to be advertised are as followed:
Party Name: (TBD... will update ASAP)
05/07/2014
10pm-close
Lineup: 'Bazzo (Akl)', 'DJ Glimtrax', 'DJ's Morquent & Pelnavo', 'Quiet Harbour Pulse'.
Dorrin Hattles Central, Corner Fenwick & Oberly Streets
$10 Tickets
R18
Tickets & Enquiries: Marta on 0219047362
Presented by Lumora Entertainment
Thanks to everyone who reads this and please give it a go! Any questions don't hesitate to ask.
Target Market(s)
New Zealand Europeans in Christchurch, New Zealand between 18 and 25 years old.
Industry/Entity Type
Events
Look and feel

```html
<!DOCTYPE html>
<html lang="en">
<head>
<meta charset="utf-8">
<title>Lorem Ipsum – Lumora Entertainment</title>
<link href="https://fonts.googleapis.com/css2?family=Orbitron:wght@900&family=Alfa+Slab+One&family=Bebas+Neue&display=swap" rel="stylesheet">
<style>
  :root {
    --night: #0b1633;
    --deep: #07102a;
    --mid-blue: #1d4d93;
    --glow: #4d8ed8;
    --white: #f4f6fb;
    --silver: #c9c9c9;
    --steel: #6e6e6e;
    --lime: #76b82a;
    --ink: #0a0a0a;
  }
  * { margin: 0; padding: 0; box-sizing: border-box; }
  html, body { width: 806px; height: 1200px; overflow: hidden; background: var(--deep); }
  .poster {
    position: relative;
    width: 806px; height: 1200px;
    overflow: hidden;
    background: linear-gradient(180deg, var(--mid-blue) 0%, #1a3b7a 40%, var(--night) 70%, var(--deep) 100%);
    font-family: 'Bebas Neue', sans-serif;
    color: var(--white);
  }
  .party-photo {
    position: absolute; left: 0; top: 140px; width: 806px; height: 560px;
    background: radial-gradient(ellipse at 50% 45%, #b79a94 0%, #7f6f86 35%, #3a4f85 65%, rgba(29,59,122,0) 85%);
  }
  .crowd-photo {
    position: absolute; left: 0; top: 900px; width: 806px; height: 300px;
    background: linear-gradient(180deg, rgba(7,16,42,0) 0%, #2f6fb8 30%, #13284f 65%, #04091a 100%);
  }
  .title {
    position: absolute; top: 62px; left: 0; width: 806px;
    text-align: center;
    font-family: 'Orbitron', sans-serif; font-weight: 900;
    font-size: 70px; letter-spacing: 6px; line-height: 1;
    color: var(--white);
    text-shadow: 0 0 18px rgba(120,170,255,.7), 0 3px 0 #8a96a8;
  }
  .presenter {
    position: absolute; top: 530px; left: 0; width: 806px;
    text-align: center;
    font-family: 'Alfa Slab One', serif;
    font-size: 56px; line-height: 66px;
    color: var(--silver);
    text-shadow: 3px 4px 4px rgba(0,0,0,.75);
  }
  .details { position: absolute; left: 0; width: 806px; text-align: center; }
  .date { top: 700px; font-size: 52px; line-height: 1; }
  .lineup { top: 790px; font-size: 25px; line-height: 32px; }
  .contact { top: 868px; font-size: 68px; line-height: 1; }
  .brand {
    position: absolute; left: 0; top: 1035px; width: 806px;
    display: flex; justify-content: center; align-items: center; gap: 14px;
    font-size: 42px; line-height: 1; color: var(--white);
  }
  .brand-square { width: 30px; height: 30px; border: 3px solid var(--white); }
  .price-sticker { position: absolute; left: 575px; top: 940px; width: 244px; height: 244px; }
</style>
</head>
<body>
<main class="poster">
  <div class="party-photo" role="img" aria-label="Photo of a group of young friends celebrating with cocktails at a party"></div>
  <div class="crowd-photo" role="img" aria-label="Photo of a nightclub crowd with raised hands under blue stage lights"></div>

  <h1 class="title">LOREM IPSUM</h1>
  <p class="presenter">Presented by Lumora<br>Entertainment</p>

  <p class="details date">10PM-CLOSE 05/07/2014</p>
  <p class="details lineup">BAZZO (AKL)', 'DJ GLIMTRAX', 'DJ'S MORQUENT &amp; PELNAVO', 'QUIET HARBOUR PULSE'.<br>DORRIN HATTLES CENTRAL, CORNER FENWICK &amp; OBERLY STREETS</p>
  <p class="details contact">MARTA ON 0219047362</p>

  <div class="brand"><span class="brand-square"></span><span>LUMORA EVENTS</span></div>

  <svg class="price-sticker" viewBox="0 0 244 244" aria-label="Tickets $10, R18">
    <circle cx="122" cy="122" r="120" fill="#ffffff"/>
    <circle cx="122" cy="122" r="108" fill="var(--lime)"/>
    <circle cx="122" cy="122" r="100" fill="none" stroke="#ffffff" stroke-width="2" stroke-dasharray="3 4"/>
    <g transform="rotate(-30 122 122)" font-family="'Bebas Neue', sans-serif" text-anchor="middle">
      <text x="118" y="118" font-size="78" fill="#ffffff">$10</text>
      <text x="126" y="178" font-size="70" fill="var(--ink)">R18</text>
    </g>
  </svg>
</main>
</body>
</html>
```